A new company focused on starting and investing in transformative businesses.

We need a simple and clean website with a few pages. we like marlowvest.com as a starting point. we want the landing page to be very simple with an option to click through on the top right into INVESTOR LOGIN. then we want to be able to scroll down to see more about our company.

Target Market(s)

professional

Coding

Coded - Design and coding required

Number of Pages Required

2 page

Font styles to use
Serif
Sans Serif

Requirements
Must have
• HALVERN BUILDERS logo (attached as a file) on the top with INVESTOR LOGIN as a click through on the right. Please model the click through from marlowvest.com. The description (also written in attached file) should be on the landing page. we do not want to have to scroll to read the description.

Then we can scroll down to read more about Halvern including the mission and the two types of businesses. More is detailed on the attached file called "Halvern Website Syntax"
Should not have
• should not be slow loading with lots of fancy graphics. should not be busy and with too many colors.

```html
<!DOCTYPE html>
<html lang="en">
<head>
<meta charset="utf-8">
<title>Halvern Builders</title>
<link rel="stylesheet" href="https://fonts.googleapis.com/css2?family=Roboto:wght@300;400;500;700&family=Arimo:wght@400;700&display=swap">
<style>
  :root {
    --ink-dark: #0e0e0e;
    --footer-dark: #151515;
    --brand-blue: #2e4690;
    --white: #ffffff;
    --body-grey: #5a5a5a;
    --heading-black: #111111;
    --rule: #2c2c2c;
  }
  * { margin: 0; padding: 0; box-sizing: border-box; }
  html, body { width: 1080px; height: 1200px; overflow: hidden; }
  body {
    position: relative;
    background: var(--white);
    font-family: "Roboto", Arial, sans-serif;
  }
  .backdrop { position: absolute; left: 0; top: 0; width: 1080px; height: 1200px; }

  .brand {
    position: absolute; left: 100px; top: 50px;
    display: flex; align-items: center; gap: 12px;
  }
  .brand-mark { width: 14px; height: 14px; background: var(--brand-blue); }
  .brand-name {
    color: var(--white); font-weight: 500; font-size: 22px; letter-spacing: 1px;
  }
  .investor-login {
    position: absolute; right: 104px; top: 50px;
    color: var(--white); font-weight: 700; font-size: 17px;
    text-decoration: underline; text-underline-offset: 3px;
  }

  .hero-statement {
    position: absolute; left: 100px; top: 218px;
    border-left: 4px solid var(--brand-blue);
    padding-left: 19px;
    color: var(--white);
    font-size: 31px; line-height: 40px; font-weight: 400;
  }
  .hero-statement strong { font-weight: 700; }
  .scroll-cue { position: absolute; left: 92px; top: 440px; }

  .mission {
    position: absolute; left: 0; top: 633px; width: 1080px;
    text-align: center;
    font-family: "Arimo", Arial, sans-serif;
    color: var(--brand-blue); font-size: 26px; line-height: 36px;
  }
  .mission strong { font-weight: 700; }

  .focus-area { position: absolute; top: 752px; width: 420px; }
  .focus-area.ground-up { left: 101px; }
  .focus-area.platform { left: 579px; }
  .focus-title { color: var(--heading-black); font-weight: 500; font-size: 20px; margin-bottom: 20px; }
  .focus-text { color: var(--body-grey); font-size: 15px; line-height: 26px; font-weight: 400; }

  .footer-info { position: absolute; left: 100px; top: 1082px; color: var(--white); }
  .footer-name { font-weight: 500; font-size: 16px; line-height: 20px; }
  .footer-contact { font-size: 14px; line-height: 20px; }
  .footer-contact a { color: var(--brand-blue); text-decoration: none; }
  .footer-rule { position: absolute; left: 100px; top: 1147px; width: 880px; height: 1px; background: var(--rule); }
  .copyright { position: absolute; left: 102px; top: 1164px; color: var(--white); font-size: 12px; }
</style>
</head>
<body>
  <svg class="backdrop" viewBox="0 0 1080 1200" aria-hidden="true">
    <defs>
      <radialGradient id="waveGlow" cx="0.55" cy="0.68" r="0.6">
        <stop offset="0" stop-color="#3a3a3c"/>
        <stop offset="0.5" stop-color="#1d1d1f"/>
        <stop offset="1" stop-color="#0e0e0e"/>
      </radialGradient>
    </defs>
    <path d="M0 0 H1080 V480 Q540 640 0 480 Z" fill="url(#waveGlow)" role="img" aria-label="Abstract wave of glowing particles across a dark background"/>
    <path d="M0 1049 Q540 913 1080 1049 V1200 H0 Z" fill="var(--footer-dark)"/>
  </svg>

  <header>
    <div class="brand">
      <span class="brand-mark"></span>
      <span class="brand-name">HALVERN BUILDERS</span>
    </div>
    <a class="investor-login" href="#">INVESTOR LOGIN</a>
  </header>

  <h1 class="hero-statement">
    <strong>Halvern Builders is an entrepreneurial firm</strong><br>
    focused on building and growing<br>
    transformational companies
  </h1>
  <svg class="scroll-cue" width="20" height="38" viewBox="0 0 20 38" aria-hidden="true">
    <path d="M10 1 V36 M2 28 L10 36 L18 28" fill="none" stroke="var(--brand-blue)" stroke-width="2"/>
  </svg>

  <p class="mission">
    Our mission is to build <strong>meaningful</strong> businesses that create <strong>enduring</strong><br>
    value by impacting people in a <strong>measurable</strong> way.
  </p>

  <section class="focus-area ground-up">
    <h2 class="focus-title">Ground Up</h2>
    <p class="focus-text">Our ground up business applies a proven analytic process to identify value edge, a form of competitive advantage. We architect transformational companies and are deliberate in creating the foundation necessary to lead an industry.</p>
  </section>
  <section class="focus-area platform">
    <h2 class="focus-title">Platform and Special Opportunities</h2>
    <p class="focus-text">We partner with exceptional teams that create value by transforming lives. Our investment focus includes large companies and spin-outs.</p>
  </section>

  <footer>
    <div class="footer-info">
      <p class="footer-name">Halvern Builders</p>
      <p class="footer-contact">For media inquiries, please contact <a href="#">press@halvernbuilders.com</a></p>
    </div>
    <div class="footer-rule"></div>
    <p class="copyright">2021 Halvern Builders &nbsp;|&nbsp; All Rights Reserved</p>
  </footer>
</body>
</html>
```